Stationary and email footer design using existing Logo design

Using the Logo design I currently have I need now to have this applied to all stationary requirements including email footer, Letter Head and footer, envelopes both window and non window ( standard letter size ).
You previously did the Logo and business cards so that's good.

```html
<!DOCTYPE html>
<html lang="en">
<head>
<meta charset="utf-8">
<title>Lilac Crest Stationery Set</title>
<link href="https://fonts.googleapis.com/css2?family=Lato:wght@400;700&display=swap" rel="stylesheet">
<style>
:root{
  --board:#d9d9d9;
  --paper:#ffffff;
  --ink:#555555;
  --ink-soft:#6e6e6e;
  --lilac:#c4a6d2;
  --stone:#c0bbb3;
  --black:#0d0d0d;
  --navy:#2b2f7a;
}
*{margin:0;padding:0;box-sizing:border-box}
html,body{width:1200px;height:1200px;overflow:hidden}
body{background:var(--board);font-family:'Lato',sans-serif;color:var(--ink);position:relative}
.sheet{position:absolute;background:var(--paper);overflow:hidden;border-top:3px solid var(--black)}
.letterhead{left:79px;top:194px;width:470px;height:664px}
.letterhead .top-fade{position:absolute;left:0;top:0;width:100%;height:90px;background:linear-gradient(#ececec,#ffffff)}
.envelope-window{left:622px;top:194px;width:511px;height:255px;border-top-width:5px}
.envelope-plain{left:622px;top:488px;width:511px;height:255px;border-top-width:5px}
.envelope-back{left:622px;top:793px;width:511px;height:255px;border-top:none}
.email-footer{left:80px;top:907px;width:468px;height:141px}

.brand{position:absolute;display:flex;align-items:center;gap:5px;color:var(--lilac);font-weight:400;letter-spacing:1.5px;text-transform:uppercase;white-space:nowrap}
.brand .mark{width:9px;height:9px;background:var(--lilac)}

.contact{position:absolute;font-size:8px;line-height:13.5px;color:var(--ink)}
.contact.right{text-align:right}
.contact .row{display:flex;align-items:center;gap:7px;justify-content:flex-end}
.contact .icon{width:8px;height:8px;fill:var(--lilac);flex:none}
.contact .gap{display:inline-block;width:8px}

.band{position:absolute;left:0;bottom:0;width:100%}

.salutation,.date{position:absolute;top:240px;font-size:7.5px}
.salutation{left:30px}
.date{right:29px}
.body-copy{position:absolute;left:30px;top:270px;width:411px;font-size:7.3px;line-height:12.6px;text-align:justify;color:var(--ink-soft)}
.body-copy p{margin-bottom:12px}
.signature{position:absolute;left:30px;top:448px;width:92px;height:30px;background:linear-gradient(90deg,rgba(43,47,122,.25),rgba(43,47,122,.08))}
.signatory{position:absolute;left:30px;top:484px}
.signatory .name{font-size:11.5px;color:#333}
.signatory .role{font-size:7.5px;color:var(--ink-soft)}

.window{position:absolute;left:43px;top:91px;width:190px;height:89px;border-radius:18px;border:3px solid #c6c6c6;background:linear-gradient(110deg,#f4f4f4,#ffffff 60%,#e6e6e6)}

.flap{position:absolute;left:0;top:0;width:100%;height:84px}

.email-contact{position:absolute;font-size:7.8px;line-height:10px;white-space:nowrap;color:var(--ink)}
.email-contact .icon{position:absolute;width:8px;height:8px;fill:var(--lilac)}
.email-contact .text{position:absolute}
.socials{position:absolute;left:169px;top:80px;display:flex;gap:4px}
.socials span{width:14px;height:14px;background:#9a9aa8}
.portrait{position:absolute;left:363px;top:22px;width:55px;height:55px;background:linear-gradient(#9fb0c0,#5b6470)}
.person{position:absolute;left:363px;top:85px;color:var(--lilac);text-transform:uppercase}
.person .name{font-size:12px;letter-spacing:.8px}
.person .role{font-size:7px;letter-spacing:.8px;color:#b49bc1}
</style>
</head>
<body>
<svg width="0" height="0" style="position:absolute">
  <defs>
    <symbol id="i-phone" viewBox="0 0 16 16"><path d="M3 1l3 3-2 2c1 2.5 3.5 5 6 6l2-2 3 3-2 2C7 14 2 9 1 3z"/></symbol>
    <symbol id="i-pin" viewBox="0 0 16 16"><path d="M8 0a5.5 5.5 0 0 1 5.5 5.5C13.5 10 8 16 8 16S2.5 10 2.5 5.5A5.5 5.5 0 0 1 8 0zm0 3a2.5 2.5 0 1 0 0 5 2.5 2.5 0 0 0 0-5z"/></symbol>
    <symbol id="i-mail" viewBox="0 0 16 16"><path d="M1 3h14v10H1zM2 4.5v.3l6 4 6-4v-.3z"/></symbol>
    <symbol id="swoosh" viewBox="0 0 760 90" preserveAspectRatio="none">
      <path d="M0 16 C320 14 560 30 680 90 L0 90Z" fill="#c0bbb3"/>
      <path d="M0 0 C330 2 620 20 760 90 L728 90 C600 32 360 8 0 6Z" fill="#c4a6d2"/>
    </symbol>
  </defs>
</svg>

<!-- Letterhead -->
<section class="sheet letterhead">
  <div class="top-fade"></div>
  <div class="brand" style="left:28px;top:98px;font-size:13px"><span class="mark"></span>Lilac Crest</div>
  <div class="contact right" style="right:29px;top:74px">
    <div class="row">08 5550 1427<svg class="icon"><use href="#i-phone"/></svg></div>
    <div class="row">Suite 4, Level 2 Harbour Court<svg class="icon"><use href="#i-pin"/></svg></div>
    <div class="row">12 Wattle Lane Kelmscott WA 6100<span class="gap"></span></div>
    <div class="row">d.reeve@lilaccrest.com.au<svg class="icon"><use href="#i-mail"/></svg></div>
  </div>
  <div class="salutation">Dear, Mr____________</div>
  <div class="date">Date : 02.07.2019</div>
  <div class="body-copy">
    <p>Lorem Ipsum is simply dummy text of the printing and typesetting industry. Lorem Ipsum has been the industry's standard dummy text ever since the1500s,when an unknown printer took a galley of type and scrambled it to make a type specimen book. It has survived not only five centuries, but also the leap into electronic typesetting, remaining essentially unchanged.</p>
    <p>Lorem Ipsum is simply dummy text of the printing and typesetting industry. Lorem Ipsum has been the industry's standard dummy text ever since the1500s.</p>
    <p>Lorem Ipsum is simply dummy text of the printing and typesetting industry.</p>
  </div>
  <div class="signature" role="img" aria-label="Handwritten signature of Daniel Reeve"></div>
  <div class="signatory">
    <div class="name">Daniel Reeve</div>
    <div class="role">Designation</div>
  </div>
  <svg class="band" height="52"><use href="#swoosh" width="100%" height="100%"/></svg>
</section>

<!-- Window envelope -->
<section class="sheet envelope-window">
  <div class="window"></div>
  <div class="brand" style="right:40px;top:82px;font-size:13px"><span class="mark"></span>Lilac Crest</div>
  <div class="contact right" style="right:36px;top:133px">
    <div class="row">08 5550 1427<svg class="icon"><use href="#i-phone"/></svg></div>
    <div class="row">Suite 4, Level 2 Harbour Court<svg class="icon"><use href="#i-pin"/></svg></div>
    <div class="row">12 Wattle Lane Kelmscott WA 6100<span class="gap"></span></div>
    <div class="row">d.reeve@lilaccrest.com.au<svg class="icon"><use href="#i-mail"/></svg></div>
  </div>
  <svg class="band" height="56"><use href="#swoosh" width="100%" height="100%"/></svg>
</section>

<!-- Standard envelope -->
<section class="sheet envelope-plain">
  <div class="brand" style="right:40px;top:82px;font-size:13px"><span class="mark"></span>Lilac Crest</div>
  <div class="contact right" style="right:36px;top:133px">
    <div class="row">08 5550 1427<svg class="icon"><use href="#i-phone"/></svg></div>
    <div class="row">Suite 4, Level 2 Harbour Court<svg class="icon"><use href="#i-pin"/></svg></div>
    <div class="row">12 Wattle Lane Kelmscott WA 6100<span class="gap"></span></div>
    <div class="row">d.reeve@lilaccrest.com.au<svg class="icon"><use href="#i-mail"/></svg></div>
  </div>
  <svg class="band" height="56"><use href="#swoosh" width="100%" height="100%"/></svg>
</section>

<!-- Envelope back -->
<section class="sheet envelope-back">
  <svg class="flap" viewBox="0 0 511 84" preserveAspectRatio="none">
    <path d="M0 0 H511 L500 64 Q497 84 478 84 H33 Q14 84 11 64Z" fill="#0d0d0d"/>
  </svg>
  <div class="brand" style="left:0;right:0;top:36px;justify-content:center;font-size:13px"><span class="mark"></span>Lilac Crest</div>
</section>

<!-- Email footer -->
<section class="sheet email-footer">
  <div class="brand" style="left:36px;top:50px;font-size:12px"><span class="mark"></span>Lilac Crest</div>
  <div class="email-contact" style="left:0;top:0">
    <svg class="icon" style="left:155px;top:34px"><use href="#i-phone"/></svg>
    <span class="text" style="left:169px;top:33px">08 5550 1427</span>
    <svg class="icon" style="left:236px;top:34px"><use href="#i-mail"/></svg>
    <span class="text" style="left:250px;top:33px">d.reeve@lilaccrest.com.au</span>
    <svg class="icon" style="left:155px;top:49px"><use href="#i-pin"/></svg>
    <span class="text" style="left:169px;top:48px">Suite 4, Level 2 Harbour Court</span>
    <span class="text" style="left:169px;top:61px">12 Wattle Lane Kelmscott WA 6100</span>
  </div>
  <div class="socials"><span></span><span></span><span></span><span></span><span></span></div>
  <div class="portrait" role="img" aria-label="Portrait photo of Daniel Reeve"></div>
  <div class="person">
    <div class="name">Daniel Reeve</div>
    <div class="role">Designation</div>
  </div>
  <svg class="band" height="34"><use href="#swoosh" width="100%" height="100%"/></svg>
</section>
</body>
</html>
```